VenuMend – Venue Emergency Magnet

We want to include a promotional magnet with our flyer to give out door-to-door. This magnet will probably live somewhere in the restaurant and needs a QR code to go to our website.
Design a high-impact promotional magnet for VenuMend to be distributed door-to-door to hospitality venues (restaurants, cafés, bars, clubs).
The magnet should:
- Be clean, bold and instantly readable.
- Feel trustworthy, modern and professional.
- Appeal specifically to hospitality venue owners and managers.
- Remain visible long-term (likely placed near POS, router, printer, office wall or fridge).
Primary Objective:
- When something breaks (POS, network, printer, internet), the venue thinks: “Call VenuMend.”
Key Message: VenuMend is the IT & POS support specialist for hospitality venues.
Design Requirements
Size: Suggested sizes (designer to mock both):
148mm x 105mm (A6 landscape)
OR 100mm x 100mm square
Rounded corners preferred.
Must Include:
- VenuMend logo
- Tagline: “Fixing Today. Helping Tomorrow.”
- Phone number (prominent): 1300 582 934
- Website: https://venumend.com.au/
- QR Code (we will supply)
Copy:
Your Hospitality Tech Doctor.
When your venue technology stops — we don’t.
• POS & EFTPOS support
• Network & Wi-Fi repairs
• Thermal printer fixes
• On-site troubleshooting
• Hospitality IT consulting
Fast. Local. Reliable.
📞 1300582934
🌐 venumend.com.au
[ QR CODE ]
Fixing today, helping tomorrow
Hospitality managers
IT Support

```html
<!DOCTYPE html>
<html lang="en">
<head>
<meta charset="utf-8">
<title>VenuMend – Venue Emergency Magnet</title>
<link rel="stylesheet" href="https://fonts.googleapis.com/css2?family=Lato:ital,wght@0,400;0,700;0,900;1,700&display=swap">
<style>
  :root {
    --teal: #2aafb5;
    --teal-light: #4cc3c6;
    --navy: #173a6b;
    --navy-deep: #12305c;
    --white: #ffffff;
    --backdrop: #d1d3d4;
  }
  * { box-sizing: border-box; margin: 0; padding: 0; }
  html, body { width: 1200px; height: 1200px; overflow: hidden; }
  body {
    background: var(--backdrop);
    font-family: "Lato", Arial, sans-serif;
    color: var(--white);
    position: relative;
  }
  .magnet { position: absolute; overflow: hidden; box-shadow: 6px 8px 14px rgba(0,0,0,0.35); }
  .magnet > svg.bg { position: absolute; inset: 0; }
  .magnet > .el { position: absolute; white-space: nowrap; }

  .brand-name { font-weight: 900; letter-spacing: -0.5px; line-height: 1; }
  .brand-sub { font-weight: 700; border-top: 1.5px solid currentColor; padding-top: 4px; margin-top: 4px; }
  .intro strong { font-weight: 700; font-style: italic; }
  .services { list-style: none; }
  .services li::before { content: "• "; }
  .contact-line { display: flex; align-items: center; gap: 10px; }
  .icon { width: 20px; height: 20px; flex: none; }

  /* A6 landscape */
  .magnet--landscape { left: 204px; top: 65px; width: 792px; height: 560px; background: var(--teal); }
  .magnet--landscape .brand { right: 43px; top: 44px; text-align: right; }
  .magnet--landscape .brand-name { font-size: 48px; }
  .magnet--landscape .brand-sub { font-size: 13px; }
  .magnet--landscape .tagline { right: 43px; top: 194px; font-size: 21px; }
  .magnet--landscape .intro { right: 43px; top: 262px; font-size: 21px; text-align: right; line-height: 1.3; }
  .magnet--landscape .services { left: 534px; top: 351px; font-size: 18.5px; line-height: 23px; }
  .magnet--landscape .contacts { left: 54px; top: 467px; font-size: 22px; line-height: 29px; }
  .magnet--landscape .promise { right: 43px; top: 497px; font-size: 21px; }

  /* Square front */
  .magnet--square-front { left: 110px; top: 661px; width: 474px; height: 474px; border-radius: 30px; background: var(--teal); }
  .magnet--square-front .brand { left: 77px; top: 58px; width: 318px; }
  .magnet--square-front .brand-name { font-size: 64px; color: var(--navy); }
  .magnet--square-front .brand-sub { font-size: 15.5px; color: var(--navy); border-top-color: var(--white); }
  .magnet--square-front .tagline { left: 0; width: 100%; text-align: center; top: 176px; font-size: 20px; }
  .magnet--square-front .icons { left: 0; width: 100%; top: 341px; display: flex; justify-content: center; gap: 7px; }
  .magnet--square-front .contacts { left: 0; width: 100%; top: 370px; text-align: center; font-size: 20px; line-height: 27px; }
  .magnet--square-front .web { letter-spacing: 2.5px; }

  /* Square back */
  .magnet--square-back { left: 618px; top: 661px; width: 472px; height: 473px; background: var(--navy); }
  .magnet--square-back .intro { left: 54px; top: 34px; font-size: 16px; line-height: 22px; }
  .magnet--square-back .intro strong { font-size: 18px; }
  .magnet--square-back .services { left: 54px; top: 99px; font-size: 16px; line-height: 20px; }
  .magnet--square-back .promise { left: 0; width: 392px; text-align: center; top: 244px; font-size: 16px; }
  .magnet--square-back .contacts { right: 52px; top: 380px; font-size: 17px; line-height: 27px; text-align: right; }
  .magnet--square-back .contact-line { justify-content: flex-end; }
</style>
</head>
<body>

<svg width="0" height="0" style="position:absolute">
  <defs>
    <symbol id="icon-phone" viewBox="0 0 20 20">
      <rect width="20" height="20" rx="4" fill="#ffffff"/>
      <path d="M6.2 4.5l2 .3.8 3-1.4 1a7 7 0 003.6 3.6l1-1.4 3 .8.3 2c0 .8-.7 1.3-1.5 1.2A10 10 0 015 6c-.1-.8.4-1.5 1.2-1.5z" fill="#173a6b"/>
    </symbol>
    <symbol id="icon-web" viewBox="0 0 20 20">
      <rect width="20" height="20" rx="4" fill="#ffffff"/>
      <g fill="none" stroke="#173a6b" stroke-width="1.3">
        <circle cx="10" cy="10" r="5.5"/>
        <ellipse cx="10" cy="10" rx="2.3" ry="5.5"/>
        <path d="M4.5 10h11M5.3 7.3h9.4M5.3 12.7h9.4"/>
      </g>
    </symbol>
  </defs>
</svg>

<!-- A6 landscape -->
<section class="magnet magnet--landscape">
  <svg class="bg" width="792" height="560" viewBox="0 0 792 560">
    <defs>
      <linearGradient id="ring-land" x1="0" y1="0" x2="1" y2="1">
        <stop offset="0" stop-color="#173a6b"/>
        <stop offset="0.55" stop-color="#1f6f95"/>
        <stop offset="1" stop-color="#2aafb5"/>
      </linearGradient>
    </defs>
    <path d="M220,0 C60,40 -40,150 -10,240 C30,360 300,430 533,458 C360,420 190,350 145,250 C105,160 170,70 310,20 L330,0 Z" fill="url(#ring-land)"/>
    <path d="M268,0 H792 V186 C620,178 420,120 268,0 Z" fill="var(--navy)"/>
  </svg>
  <div class="el brand">
    <div class="brand-name">VenuMend</div>
    <div class="brand-sub">Hospitality IT, POS &amp; Network Specialists</div>
  </div>
  <p class="el tagline">Fixing Today. Helping Tomorrow.</p>
  <p class="el intro"><strong>Your Hospitality Tech Doctor.</strong><br>When your venue technology stops — we don’t.</p>
  <ul class="el services">
    <li>POS &amp; EFTPOS support</li>
    <li>Network &amp; Wi-Fi repairs</li>
    <li>Thermal printer fixes</li>
    <li>On-site troubleshooting</li>
    <li>Hospitality IT consulting</li>
  </ul>
  <div class="el contacts">
    <div class="contact-line"><svg class="icon"><use href="#icon-phone"/></svg>1300 582 934</div>
    <div class="contact-line"><svg class="icon"><use href="#icon-web"/></svg>venumend.com.au</div>
  </div>
  <p class="el promise">Fast. Local. Reliable.</p>
</section>

<!-- Square front -->
<section class="magnet magnet--square-front">
  <svg class="bg" width="474" height="474" viewBox="0 0 474 474">
    <defs>
      <linearGradient id="tab-front" x1="0" y1="0" x2="1" y2="0">
        <stop offset="0" stop-color="#2aafb5"/>
        <stop offset="1" stop-color="#1d7fa0"/>
      </linearGradient>
    </defs>
    <path d="M285,262 L398,249 Q418,247 421,267 L428,330 L285,310 Z" fill="url(#tab-front)"/>
    <path d="M0,474 V330 Q0,262 55,258 L418,318 Q450,324 458,352 L474,420 V474 Z" fill="var(--navy)"/>
  </svg>
  <div class="el brand">
    <div class="brand-name">VenuMend</div>
    <div class="brand-sub">Hospitality IT, POS &amp; Network Specialists</div>
  </div>
  <p class="el tagline">Fixing Today. Helping Tomorrow.</p>
  <div class="el icons">
    <svg class="icon"><use href="#icon-phone"/></svg>
    <svg class="icon"><use href="#icon-web"/></svg>
  </div>
  <div class="el contacts">
    <div>1300 582 934</div>
    <div class="web">venumend.com.au</div>
  </div>
</section>

<!-- Square back -->
<section class="magnet magnet--square-back">
  <svg class="bg" width="472" height="473" viewBox="0 0 472 473">
    <defs>
      <linearGradient id="wall-back" x1="0" y1="0" x2="0" y2="1">
        <stop offset="0" stop-color="#4cc3c6"/>
        <stop offset="1" stop-color="#173a6b"/>
      </linearGradient>
    </defs>
    <path d="M415,0 H472 C462,170 360,345 200,350 C330,320 430,170 415,0 Z" fill="url(#wall-back)" opacity="0.8"/>
    <path d="M0,0 H446 C440,160 330,335 196,340 C110,343 40,290 0,200 Z" fill="var(--teal)"/>
  </svg>
  <p class="el intro"><strong>Your Hospitality Tech Doctor.</strong><br>When your venue technology stops — we don’t.</p>
  <ul class="el services">
    <li>POS &amp; EFTPOS support</li>
    <li>Network &amp; Wi-Fi repairs</li>
    <li>Thermal printer fixes</li>
    <li>On-site troubleshooting</li>
    <li>Hospitality IT consulting</li>
  </ul>
  <p class="el promise">Fast. Local. Reliable.</p>
  <div class="el contacts">
    <div class="contact-line">1300 582 934<svg class="icon"><use href="#icon-phone"/></svg></div>
    <div class="contact-line">venumend.com.au<svg class="icon"><use href="#icon-web"/></svg></div>
  </div>
</section>

</body>
</html>
```